SilverLedgerOak - Double Sided Business Card

We are looking for design options or our business cards. We are a Business Solutions and HR solutions Provider - the theme is business, for this card.

Our brand colours are represented within our logo.

Details needed to be put on the front of the business card are:

Employees name: [Sample Name]
Role: [Sample Role]

Address: Suite 4 - Level 3/48 Halloran Avenue Parramatta NSW 2150
M: 0000 000 000
P: 1300 847 213
F: 1300 847 286
E: sample@silverledgeroak.com.au
www.silverledgeroak.com.au
Updates

Reason: Hello, could we please increase our deadline by 5 days. Thanking you, Tess

Target Market(s)

Business Owners, also Candidates looking for Employment

Industry/Entity Type

Business

Contact Information for Business Card

Role: [Sample Role]

M: 0000 000 000
P: 1300 847 213
F: 1300 847 286

Font styles to use
Sans Serif

Colors
3276b5
3176b5
0455a3
85abd2
cfdeed
ffffff
000000
1b1b1b
757575

Requirements
Must have
• Details needed to be put on the front of the business card are:
• Employees name: [Sample Name]
• Role: [Sample Role]
• Address: Suite 4 - Level 3/48 Halloran Avenue Parramatta NSW 2150
• M: 0000 000 000
• P: 1300 847 213
• F: 1300 847 286
• E: sample@silverledgeroak.com.au
• www.silverledgeroak.com.au
Nice to have
• Simplicity, clean and professional.

```html
<!DOCTYPE html>
<html lang="en">
<head>
<meta charset="utf-8">
<title>SilverLedgerOak – Business Card</title>
<link href="https://fonts.googleapis.com/css2?family=Lato:wght@400;700&family=Montserrat:wght@700&display=swap" rel="stylesheet">
<style>
  :root {
    --brand-blue: #0d55a3;
    --brand-navy: #142a4a;
    --ink: #1b1b1b;
    --muted: #757575;
    --paper: #ffffff;
    --backdrop: #eeeeee;
  }
  * { box-sizing: border-box; margin: 0; padding: 0; }
  html, body { width: 1200px; height: 586px; overflow: hidden; }
  body { background: var(--backdrop); position: relative; font-family: "Lato", Arial, sans-serif; }

  .card { position: absolute; top: 129px; width: 502px; height: 300px; }
  .card--front { left: 61px; background: var(--brand-blue); color: var(--paper); }
  .card--back { left: 619px; background: var(--paper); color: var(--ink); overflow: hidden; }

  .brand-mark { display: block; background: currentColor; }

  .front-brand { position: absolute; left: 0; right: 0; top: 40px; text-align: center; }
  .front-brand .brand-mark { width: 72px; height: 72px; margin: 0 auto 22px; color: var(--paper); }
  .front-brand .brand-name { font-family: "Montserrat", Arial, sans-serif; font-weight: 700; font-size: 29px; letter-spacing: 0.5px; }
  .front-brand .brand-rule { width: 282px; height: 1px; background: var(--paper); margin: 8px auto 9px; opacity: .9; }
  .front-brand .tagline { font-family: Arial, Helvetica, sans-serif; font-weight: 700; font-size: 10.5px; }
  .website { position: absolute; left: 0; right: 0; top: 257px; text-align: center; font-weight: 700; font-size: 12.5px; }

  .back-brand { position: absolute; right: 30px; top: 20px; width: 180px; text-align: center; color: var(--brand-navy); }
  .back-brand .brand-mark { width: 60px; height: 60px; margin: 0 auto 12px; color: var(--brand-blue); }
  .back-brand .brand-name { font-family: "Montserrat", Arial, sans-serif; font-weight: 700; font-size: 16px; color: var(--brand-navy); }
  .back-brand .brand-rule { height: 1px; background: var(--brand-navy); margin: 5px 4px 5px; }
  .back-brand .tagline { font-family: Arial, Helvetica, sans-serif; font-weight: 700; font-size: 6.5px; color: var(--ink); white-space: nowrap; }

  .person { position: absolute; left: 28px; top: 100px; }
  .person-name { font-family: "Montserrat", Arial, sans-serif; font-weight: 700; font-size: 17px; color: var(--brand-navy); }
  .person-role { font-size: 11.5px; color: var(--muted); margin-top: 3px; }

  .contact-list { position: absolute; left: 28px; top: 166px; list-style: none; }
  .contact-list li { display: flex; align-items: center; height: 22px; font-size: 12px; }
  .contact-icon { width: 17px; height: 17px; margin-right: 6px; flex: none; }
  .contact-label { font-weight: 700; color: var(--brand-blue); margin-right: 4px; }

  .base-band { position: absolute; left: 0; bottom: 0; width: 502px; height: 16px; }
</style>
</head>
<body>

<section class="card card--front" aria-label="Card front">
  <div class="front-brand">
    <span class="brand-mark" aria-hidden="true"></span>
    <p class="brand-name">SilverLedgerOak</p>
    <div class="brand-rule"></div>
    <p class="tagline">Helping small to medium business realise their potential</p>
  </div>
  <p class="website">www.silverledgeroak.com.au</p>
</section>

<section class="card card--back" aria-label="Card back">
  <div class="back-brand">
    <span class="brand-mark" aria-hidden="true"></span>
    <p class="brand-name">SilverLedgerOak</p>
    <div class="brand-rule"></div>
    <p class="tagline">Helping small to medium business realise their potential</p>
  </div>

  <div class="person">
    <p class="person-name">[Sample Name]</p>
    <p class="person-role">[Sample Role]</p>
  </div>

  <ul class="contact-list">
    <li>
      <svg class="contact-icon" viewBox="0 0 20 20" aria-hidden="true"><circle cx="10" cy="10" r="10" fill="#0d55a3"/><rect x="7" y="4.5" width="6" height="11" rx="1" fill="#fff"/><rect x="8" y="6" width="4" height="7" fill="#0d55a3"/></svg>
      <span class="contact-label">M:</span>0000 000 000
    </li>
    <li>
      <svg class="contact-icon" viewBox="0 0 20 20" aria-hidden="true"><circle cx="10" cy="10" r="10" fill="#0d55a3"/><path d="M6 8.5c0-1.5 1.8-2.5 4-2.5s4 1 4 2.5h-2v-1H8v1zM6.5 10h7l.5 4H6z" fill="#fff"/></svg>
      <span class="contact-label">P:</span>1300 847 213
    </li>
    <li>
      <svg class="contact-icon" viewBox="0 0 20 20" aria-hidden="true"><circle cx="10" cy="10" r="10" fill="#0d55a3"/><path d="M7 5h6v3H7zM5 9h10v5h-2v-2H7v2H5zM7.5 12.5h5V15h-5z" fill="#fff"/></svg>
      <span class="contact-label">F:</span>1300 847 286
    </li>
    <li>
      <svg class="contact-icon" viewBox="0 0 20 20" aria-hidden="true"><circle cx="10" cy="10" r="10" fill="#0d55a3"/><rect x="5" y="6.5" width="10" height="7" fill="#fff"/><path d="M5 6.5l5 4 5-4" fill="none" stroke="#0d55a3" stroke-width="1"/></svg>
      sample@silverledgeroak.com.au
    </li>
    <li>
      <svg class="contact-icon" viewBox="0 0 20 20" aria-hidden="true"><circle cx="10" cy="10" r="10" fill="#0d55a3"/><rect x="7" y="4.5" width="6" height="11" fill="#fff"/><path d="M8.3 6h1.2M10.5 6h1.2M8.3 8h1.2M10.5 8h1.2M8.3 10h1.2M10.5 10h1.2M8.3 12h1.2M10.5 12h1.2" stroke="#0d55a3" stroke-width=".9"/></svg>
      Suite 4 - Level 3/48 Halloran Avenue Parramatta NSW 2150
    </li>
  </ul>

  <svg class="base-band" viewBox="0 0 502 16" preserveAspectRatio="none" aria-hidden="true">
    <rect x="0" y="3" width="502" height="13" fill="#142a4a"/>
    <path d="M298 16 C304 4 312 0 330 0 H502 V16 Z" fill="#ffffff"/>
    <path d="M304 16 C310 6 318 2 334 2 H502 V16 Z" fill="#0d55a3"/>
  </svg>
</section>

</body>
</html>
```